100% West Australian Static Banner

I require a static banner to go on a couple of pages in our website (under development) that highlights that we are a 100% Western Australian Owned & Operated company. I would prefer the banner to be in our company colours (blue shades & grey). I also would like it to be eye catching and modern in design. I have included a 100% West Australian rubber stamp logo to be used as well as including our logo so you know our colours. The banner needs to be 1139 x 350 pixels in size.

Target Market(s)

B2B

Requirements
Must have
• Our rubber stamp 100% West Australian logo
• Modern Eye Catching design
• Blue shaded background
Nice to have
• Shading background similar our logo blue colours
• 100% logo can be reversed out if required or colour changed
• Larger text saying - 100% West Australian Owned & Operated

```html
<!DOCTYPE html>
<html lang="en">
<head>
<meta charset="utf-8">
<title>100% West Australian Owned &amp; Operated Banner</title>
<link rel="stylesheet" href="https://fonts.googleapis.com/css2?family=Roboto+Condensed:wght@400;700&display=swap">
<style>
  :root {
    --bg-top: #eef1f8;
    --bg-mid: #d2dbea;
    --bg-low: #aebbd3;
    --navy: #2e3192;
    --grey: #666a70;
    --brand-grey: #6e7f9c;
    --wave-pale: #a9d3f3;
    --wave-light: #5cb6ec;
    --wave-mid: #2f95e0;
    --wave-deep: #1766d6;
    --wave-line: rgba(255,255,255,0.7);
    --badge: #1f6fc4;
  }
  html, body {
    margin: 0;
    padding: 0;
    width: 1200px;
    height: 369px;
    overflow: hidden;
  }
  .banner {
    position: relative;
    width: 1200px;
    height: 369px;
    overflow: hidden;
    background: linear-gradient(160deg, var(--bg-top) 0%, var(--bg-mid) 45%, var(--bg-low) 100%);
    font-family: "Roboto Condensed", "Arial Narrow", sans-serif;
  }
  .waves {
    position: absolute;
    inset: 0;
    width: 1200px;
    height: 369px;
  }
  .brand {
    position: absolute;
    left: 42px;
    top: 36px;
    display: flex;
    align-items: center;
    gap: 14px;
  }
  .brand-dot {
    width: 54px;
    height: 54px;
    border-radius: 50%;
    background: var(--brand-grey);
  }
  .brand-name {
    font-size: 25px;
    font-weight: 400;
    color: var(--brand-grey);
    letter-spacing: 0.3px;
  }
  .headline {
    position: absolute;
    left: 188px;
    top: 138px;
    margin: 0;
  }
  .headline-main {
    display: block;
    font-size: 58px;
    font-weight: 700;
    line-height: 1;
    color: var(--navy);
  }
  .headline-sub {
    display: block;
    margin-top: 8px;
    font-size: 36px;
    font-weight: 700;
    line-height: 1;
    color: var(--grey);
  }
  .badge {
    position: absolute;
    right: 30px;
    top: 8px;
    width: 132px;
    height: 132px;
    border-radius: 50%;
    background: var(--badge);
    box-shadow: 0 0 0 5px #fff, 0 0 0 8px var(--badge);
  }
</style>
</head>
<body>
  <div class="banner">
    <svg class="waves" viewBox="0 0 1200 369" aria-hidden="true">
      <path fill="var(--wave-pale)" d="M0 190 C150 240 260 320 430 322 C650 324 820 185 1010 165 C1100 157 1160 165 1200 172 L1200 369 L0 369 Z"/>
      <path fill="var(--wave-light)" d="M0 212 C160 280 290 350 470 346 C700 340 860 215 1050 198 C1120 193 1170 198 1200 204 L1200 369 L0 369 Z"/>
      <path fill="var(--wave-mid)" d="M0 250 C170 320 320 369 520 369 L1200 369 L1200 240 C1050 230 900 280 760 330 C680 355 600 369 520 369 Z"/>
      <path fill="var(--wave-deep)" d="M520 369 C700 369 860 270 1020 245 C1100 233 1160 240 1200 248 L1200 369 Z"/>
      <path fill="none" stroke="var(--wave-line)" stroke-width="2" d="M0 200 C160 258 280 336 450 334 C680 330 840 200 1030 182 C1110 175 1165 182 1200 188"/>
      <path fill="none" stroke="var(--wave-line)" stroke-width="1.5" d="M0 232 C170 300 310 362 500 358 C720 352 870 236 1060 220 C1125 215 1170 220 1200 226"/>
      <path fill="none" stroke="var(--wave-line)" stroke-width="1.5" d="M640 369 C780 300 900 250 1040 232 C1110 224 1165 228 1200 234"/>
    </svg>

    <div class="brand">
      <span class="brand-dot"></span>
      <span class="brand-name">CoreCrate</span>
    </div>

    <h1 class="headline">
      <span class="headline-main">100% West Australian</span>
      <span class="headline-sub">Owned &amp; Operated</span>
    </h1>

    <div class="badge" role="img" aria-label="Locally owned stamp badge"></div>
  </div>
</body>
</html>
```